Business Card for Multi-Brand Sportswear Company

We are looking for a business card which represents our company and the multiple brands within it.

The company: Kelt Athletic (LTD)
The brands: Kelt, PawaLuni, VerdantFlex, Grit and Gale

Employees using these cards would be representing Kelt Athletic, rather than any of the individual brands. You will see a current design within the uploaded files, to give some inspiration. The actual text of the brands is not necessary, but the logos should be on there is some format.

Our creative minds on this are stretched, so we are looking for someone to make this their own, and show us what a good business card should look like.

We may like to get these printed with spot gloss, so keep that in mind with your designs.

www.keltathletic.co.uk

Industry/Entity Type

Business

Contact Information for Business Card

Tom Hollingsworth-Pryce
Operations Manager
(+44) 1632 960 418
Tom@keltathletic.co.uk
www.keltathletic.co.uk

Font styles to use
Sans Serif
Other font styles liked:
• Eurostile

Colors
ffffff

Requirements
Nice to have
• Dark (black) background

```html
<!DOCTYPE html>
<html lang="en">
<head>
<meta charset="utf-8">
<title>Kelt Athletic – Business Card</title>
<link href="https://fonts.googleapis.com/css2?family=Michroma&family=Archivo:wght@400;600;700&display=swap" rel="stylesheet">
<style>
  :root {
    --stage: #1a1a1a;
    --card: #121212;
    --white: #ffffff;
    --red: #e3191f;
    --silver: #a9a9a9;
    --muted: #6a6a6a;
    --rule: #4a4a4a;
  }
  * { margin: 0; padding: 0; box-sizing: border-box; }
  html, body { width: 1200px; height: 900px; overflow: hidden; background: var(--stage); }
  .stage {
    width: 1200px; height: 900px;
    display: flex; flex-direction: column; align-items: center; justify-content: center; gap: 40px;
  }
  .card {
    width: 580px; height: 350px; background: var(--card);
    position: relative; box-shadow: 0 12px 30px rgba(0,0,0,.55);
    font-family: "Archivo", Arial, sans-serif; color: var(--white);
  }
  /* front */
  .identity { position: absolute; left: 48px; top: 112px; width: 250px; text-align: right; }
  .identity__name { font-family: "Michroma", sans-serif; font-size: 21px; letter-spacing: .5px; white-space: nowrap; }
  .identity__role { color: var(--red); font-weight: 600; font-size: 14px; margin-top: 6px; }
  .divider { position: absolute; left: 318px; top: 92px; width: 1px; height: 90px; background: var(--rule); }
  .contact { position: absolute; left: 338px; top: 96px; list-style: none; }
  .contact li { display: flex; align-items: center; gap: 12px; font-size: 13px; height: 27px; white-space: nowrap; }
  .contact svg { width: 14px; height: 14px; fill: var(--red); flex: none; }
  .contact .accent { color: var(--red); }
  .address { position: absolute; left: 0; right: 0; bottom: 62px; display: flex; justify-content: center; align-items: center; gap: 10px; font-size: 13px; font-weight: 600; letter-spacing: .3px; }
  .address svg { width: 12px; height: 16px; fill: var(--red); }
  /* back */
  .brandmark { position: absolute; left: 0; right: 0; top: 92px; text-align: center; }
  .brandmark__name { font-family: "Michroma", sans-serif; font-size: 40px; color: var(--silver); letter-spacing: 1px; }
  .brandmark__tag { font-size: 12px; letter-spacing: 4px; color: var(--muted); margin-top: 10px; text-transform: uppercase; }
  .brand-row { position: absolute; left: 0; right: 0; top: 236px; display: flex; justify-content: center; gap: 30px; list-style: none; }
  .brand-row li { font-family: "Michroma", sans-serif; font-size: 12px; color: var(--muted); white-space: nowrap; }
</style>
</head>
<body>
<main class="stage">
  <section class="card card--front">
    <div class="identity">
      <h1 class="identity__name">RHYS DENHOLM</h1>
      <p class="identity__role">Managing Director</p>
    </div>
    <div class="divider"></div>
    <ul class="contact">
      <li><svg viewBox="0 0 24 24"><path d="M6.6 10.8a15 15 0 0 0 6.6 6.6l2.2-2.2a1 1 0 0 1 1-.25 11.4 11.4 0 0 0 3.6.57 1 1 0 0 1 1 1V20a1 1 0 0 1-1 1A17 17 0 0 1 3 4a1 1 0 0 1 1-1h3.5a1 1 0 0 1 1 1c0 1.25.2 2.45.57 3.57a1 1 0 0 1-.25 1z"/></svg>+44(0)1632960418</li>
      <li><svg viewBox="0 0 24 24"><path d="M2 5h20v14H2z M2 5l10 8 10-8" /></svg>rhys@keltathletic.co.uk</li>
      <li><svg viewBox="0 0 24 24"><circle cx="12" cy="12" r="10"/></svg>www.<span class="accent">keltathletic</span>.co.uk</li>
    </ul>
    <p class="address"><svg viewBox="0 0 12 16"><path d="M6 0a6 6 0 0 0-6 6c0 4.5 6 10 6 10s6-5.5 6-10a6 6 0 0 0-6-6zm0 8.5A2.5 2.5 0 1 1 6 3.5a2.5 2.5 0 0 1 0 5z"/></svg>Harrow Fold, Kelby, Northby, NB04 2QX</p>
  </section>

  <section class="card card--back">
    <div class="brandmark">
      <p class="brandmark__name">Kelt Athletic</p>
      <p class="brandmark__tag">Performance Wear</p>
    </div>
    <ul class="brand-row">
      <li>Grit and Gale</li>
      <li>VerdantFlex</li>
      <li>Kelt</li>
      <li>PawaLuni</li>
    </ul>
  </section>
</main>
</body>
</html>
```